Quorlapex

Hi everyone!

Looks like our project is more sophisticated than we expected. So good news - we increased the budget! and one of you will sure get the prize - no money back for us!

We are a young Russian company that specializes in in-taxi entertainment. We believe that our key strength is great attention to user experience. We've devoted much effort to improve ergonomics of our devices - tablet PCs that we install in the taxis. And yes, we enjoy to simplify things!

Now we need the most basic things - a logo and some staff for client meetings (primarily advertisers and ad agencies).

As for logo - we already have one engraved on the prototypes of our device (see attached file). This is one of the ideas (still far from perfect) - what we appreciate in it is minimalistic yet stylish approach.

As for "take it to the meeting stuff" we want to start with name card, pen and notepad (A4) that we will leave in clients's office, also as a reminder. Shall your have more smart ideas - always welcome!

As for logo and name cards - we would like to make an image of serious but modern company. Our design should communicate creativity and reliability. We believe that "to understand is to simplify" - minimalistic design is the most difficult one. Its better to work hard on fonts and arrangement, than put 10 variegated images.

SO THE TASK IS TO DESIGN:
- a logo
- a name card
- a note pad (great example in attachment)
- a pen

Shall you have more questions - please ask in comments.

We look forward to meeting like-minded fellows here!

Target Market(s)

Out target are:

- advertiser
- advertising agencies
- taxi passenger

Industry/Entity Type

It Company

Requirements
Must have
• font should be chosen very carefully
Nice to have
• classic minimalistic plain text only but very stylish name card is a dream of one of our co-founders:)
Should not have
• we do not want to have taxi-like colors and chess-boards. We are closer to "innovation", "entertainment", and "user experience", rather than "taxi".

```html
<!DOCTYPE html>
<html lang="en">
<head>
<meta charset="utf-8">
<title>Quorlapex Notepad</title>
<link rel="stylesheet" href="https://fonts.googleapis.com/css2?family=Michroma&display=swap">
<style>
  :root {
    --backdrop: #ffffff;
    --paper: #efefee;
    --paper-edge: #dcdcda;
    --sheet: #f6f6f4;
    --grid: #cfd6dc;
    --grid-frame: #b9c2ca;
    --rule: #3a3a3a;
    --brand: #f07a26;
  }
  * { box-sizing: border-box; margin: 0; padding: 0; }
  html, body {
    width: 1200px; height: 900px; overflow: hidden;
    background: var(--backdrop);
  }
  .notepad {
    position: relative; width: 1200px; height: 900px;
  }
  .page {
    position: absolute; top: 70px; width: 537px; height: 760px;
    border: 1px solid var(--paper-edge);
  }
  .cover { left: 30px; background: var(--paper); }
  .sheet { left: 633px; background: var(--sheet); }

  .brand-band {
    position: absolute; left: 0; right: 0;
    display: flex; flex-direction: column; align-items: center;
  }
  .brand-band .rule {
    height: 2px; background: var(--rule); border-radius: 2px;
  }
  .brand-name {
    font-family: "Michroma", sans-serif;
    font-weight: 400;
    color: var(--brand);
    text-transform: uppercase;
    line-height: 1;
  }

  .cover .brand-band { top: 95px; gap: 22px; }
  .cover .rule { width: 440px; }
  .cover .brand-name { font-size: 50px; letter-spacing: 2px; }

  .peephole {
    position: absolute; left: 246px; top: 470px;
    width: 44px; height: 44px; border-radius: 50%;
    background-color: var(--sheet);
    background-image:
      linear-gradient(var(--grid) 1px, transparent 1px),
      linear-gradient(90deg, var(--grid) 1px, transparent 1px);
    background-size: 9px 9px;
    box-shadow: inset 0 1px 3px rgba(0,0,0,0.25);
  }

  .grid-area {
    position: absolute; left: 38px; right: 38px; top: 60px; bottom: 130px;
    border: 1px solid var(--grid-frame);
    background-image:
      linear-gradient(var(--grid) 1px, transparent 1px),
      linear-gradient(90deg, var(--grid) 1px, transparent 1px);
    background-size: 13px 13px;
  }
  .sheet .brand-band {
    left: auto; right: 38px; bottom: 40px; width: 230px; gap: 10px;
  }
  .sheet .rule { width: 230px; height: 1.5px; }
  .sheet .brand-name { font-size: 22px; letter-spacing: 1px; }
</style>
</head>
<body>
<main class="notepad">
  <section class="page cover">
    <div class="brand-band">
      <span class="rule"></span>
      <span class="brand-name">Quorlapex</span>
      <span class="rule"></span>
    </div>
    <span class="peephole"></span>
  </section>

  <section class="page sheet">
    <div class="grid-area"></div>
    <div class="brand-band">
      <span class="rule"></span>
      <span class="brand-name">Quorlapex</span>
      <span class="rule"></span>
    </div>
  </section>
</main>
</body>
</html>
```